Referral Flyer Marketing Flyer 8.5" x 5.5" (Half Page) Front & Back

Designer Instructions – Updated Referral Program Flyer

(Based on the mock-up in “Brief Layout and Instructions.pdf”)

OVERALL STYLE + LAYOUT

Maintain the same general layout, structure, and flow as the mock-up flyer (front and back).

This is an update of an older flyer, not a full redesign — keep the same sections, proportions, and overall visual feel, but with cleaner, more modern design improvements.

The final flyer should look clean, bold, professional, and high-impact, geared toward realtors, property managers, and contractors who refer work.

FRONT SIDE INSTRUCTIONS
1. Header Section

Remove the Tidewell Renovation logo from the top banner.
(Shown on page 1 of the PDF)

2. Main Headline

Keep the same three-line structure:
EARN
UNLIMITED
CASH

Center it, maximize impact, and increase the font size of CASH so all three words match in importance.

Make the headline bold, clean, and the main focal point.

3. Cash Incentive Box

Keep the "$500 minimum OR 10% per referral" box, but upgrade the graphics to look sharper and more modern.

Ensure the wording matches exactly what’s in the mock-up.

4. Premier Partner Program Ribbon

Clean up and modernize the "PREMIER PARTNER PROGRAM" bar while keeping the same position and structure.

Ensure the checkmark badge remains crisp and professional.

5. Supporting Icons Section

Keep the four icons/benefit boxes (Guaranteed Payout, Free Evaluations, Affordable Solutions, Industry Leaders) in the same order.

Update the icons to cleaner, more modern styles — but maintain the same meanings.

Improve alignment and spacing for sharper visual consistency.

6. Remove Icons in Contact Area

At the bottom (“CALL TEXT OR BOOK ONLINE 858-472-6190 BrightKeelRebuilds.com”), remove the phone and internet icons, as noted on page 2 of the PDF.

7. Replace All Images

I (Dorian) will provide all updated stock images separately via email.

Replace the flood/water-damage imagery and roof leak with the new images I send.

Keep image placement and proportions the same as the mock-up.

BACK SIDE INSTRUCTIONS
1. Header Image + “REFER / EARN” Section

Maintain the same large split-image layout (“The more you refer, the more you earn”).

Replace all background imagery with the new assets I will send.

Keep the CASH FLOW image section but modernize the type and spacing.

2. “HOW IT WORKS” Section

Preserve the three-column layout:

Refer Flood, Water & Mold Damage

We Take Care of Everything (evaluations/insurance)

Get Paid to Share

Update images, tighten spacing, and use modern iconography.

3. Remove Phone/Internet Icons

Same as the front side — remove small communication icons and keep only the text/number/URL.

4. Bottom Contact Bar

Keep the blue bar, same wording, same layout — just modernize the style if needed for clarity.

5. Replace All Back-Side Images

Again, I will email you the image assets.

Keep the layout EXACT — just update with higher-quality photos and improved design.

TEXT CONTENT (Keep as-is unless spacing adjustments needed)

All text shown in the PDF should remain exactly the same unless spacing or visual balance requires minor adjustments.
Example from page 3:

“REFER FLOOD, MOLD & CONSTRUCTION JOBS”

“We Schedule a Free Estimate. If Approved, You Get Paid.”

“Everybody Benefits From Referrals”

Everything stays, just refreshed and visually improved.

DESIGN GOALS

Flyer should look high-end and trustworthy, not salesy.

Consistent color theme: blues, whites, yellows, same palette as original.

Use bold, modern fonts with strong readability.

Ensure all headlines pop and all benefit boxes are clean, well-aligned, and evenly spaced.

The final result should feel like a premium referral program flyer for a top-tier restoration/remodel company.

FILES I WILL PROVIDE

I will send the designer:

All replacement stock photos

Any updated logos (if needed)

Original high-resolution version of the mock-up (if available)

Any additional icons preferred

Colors
0054AA
0677BA
7BADD7
CADEEF
E8F1F8

Requirements
Must have
• Designer Instructions – Updated Referral Program Flyer (Based on the mock-up in “Brief Layout and Instructions.pdf”) OVERALL STYLE + LAYOUT Maintain the same general layout, structure, and flow as the mock-up flyer (front and back). This is an update of an older flyer, not a full redesign — keep the same sections, proportions, and overall visual feel, but with cleaner, more modern design improvements. The final flyer should look clean, bold, professional, and high-impact, geared toward realtors, property managers, and contractors who refer work. FRONT SIDE INSTRUCTIONS 1. Header Section Remove the Tidewell Renovation logo from the top banner. (Shown on page 1 of the PDF) 2. Main Headline Keep the same three-line structure: EARN UNLIMITED CASH Center it, maximize impact, and increase the font size of CASH so all three words match in importance. Make the headline bold, clean, and the main focal point. 3. Cash Incentive Box Keep the "$500 minimum OR 10% per referral" box, but upgrade the graphics to look sharper and more modern. Ensure the wording matches exactly what’s in the mock-up. 4. Premier Partner Program Ribbon Clean up and modernize the "PREMIER PARTNER PROGRAM" bar while keeping the same position and structure. Ensure the checkmark badge remains crisp and professional. 5. Supporting Icons Section Keep the four icons/benefit boxes (Guaranteed Payout, Free Evaluations, Affordable Solutions, Industry Leaders) in the same order. Update the icons to cleaner, more modern styles — but maintain the same meanings. Improve alignment and spacing for sharper visual consistency. 6. Remove Icons in Contact Area At the bottom (“CALL TEXT OR BOOK ONLINE 858-472-6190 BrightKeelRebuilds.com”), remove the phone and internet icons, as noted on page 2 of the PDF. 7. Replace All Images I (Dorian) will provide all updated stock images separately via email. Replace the flood/water-damage imagery and roof leak with the new images I send. Keep image placement and proportions the same as the mock-up. BACK SIDE INSTRUCTIONS 1. Header Image + “REFER / EARN” Section Maintain the same large split-image layout (“The more you refer, the more you earn”). Replace all background imagery with the new assets I will send. Keep the CASH FLOW image section but modernize the type and spacing. 2. “HOW IT WORKS” Section Preserve the three-column layout: Refer Flood, Water & Mold Damage We Take Care of Everything (evaluations/insurance) Get Paid to Share Update images, tighten spacing, and use modern iconography. 3. Remove Phone/Internet Icons Same as the front side — remove small communication icons and keep only the text/number/URL. 4. Bottom Contact Bar Keep the blue bar, same wording, same layout — just modernize the style if needed for clarity. 5. Replace All Back-Side Images Again, I will email you the image assets. Keep the layout EXACT — just update with higher-quality photos and improved design. TEXT CONTENT (Keep as-is unless spacing adjustments needed) All text shown in the PDF should remain exactly the same unless spacing or visual balance requires minor adjustments. Example from page 3: “REFER FLOOD, MOLD & CONSTRUCTION JOBS” “We Schedule a Free Estimate. If Approved, You Get Paid.” “Everybody Benefits From Referrals” Everything stays, just refreshed and visually improved. DESIGN GOALS Flyer should look high-end and trustworthy, not salesy. Consistent color theme: blues, whites, yellows, same palette as original. Use bold, modern fonts with strong readability. Ensure all headlines pop and all benefit boxes are clean, well-aligned, and evenly spaced. The final result should feel like a premium referral program flyer for a top-tier restoration/remodel company. FILES I WILL PROVIDE I will send the designer: All replacement stock photos Any updated logos (if needed) Original high-resolution version of the mock-up (if available) Any additional icons preferred

```html
<!DOCTYPE html>
<html lang="en">
<head>
<meta charset="utf-8">
<title>Referral Program Flyer – Front &amp; Back</title>
<link rel="stylesheet" href="https://fonts.googleapis.com/css2?family=Archivo+Black&family=Montserrat:wght@600;700;800;900&family=Roboto:wght@400;500;700&display=swap">
<style>
:root{
  --blue-deep:#0054AA;
  --blue-mid:#0677BA;
  --blue-soft:#7BADD7;
  --blue-pale:#CADEEF;
  --blue-mist:#E8F1F8;
  --navy:#0a3b86;
  --yellow:#F6C407;
  --red:#C8161D;
  --gold:#B38A17;
  --gray:#9a9ea4;
  --ink:#1d2733;
  --white:#ffffff;
  --page:#f3f4f6;
}
*{box-sizing:border-box;margin:0;padding:0}
html,body{width:1200px;height:914px;overflow:hidden}
body{background:var(--page);position:relative;font-family:"Montserrat",sans-serif}

.flyer{position:absolute;width:660px;height:427px;background:var(--white);overflow:hidden;box-shadow:0 6px 18px rgba(0,0,0,.12)}
.flyer--back{left:500px;top:20px}
.flyer--front{left:40px;top:467px}
.abs{position:absolute}

/* ---------- shared contact bar ---------- */
.contact-bar{position:absolute;left:0;right:0;bottom:0;height:27px;background:var(--blue-soft);display:flex;align-items:center;justify-content:center;gap:14px}
.contact-bar__label{font:600 12px "Montserrat",sans-serif;color:var(--ink);letter-spacing:.3px}
.contact-bar__phone{font:700 18px "Montserrat",sans-serif;color:var(--ink);letter-spacing:.5px}
.contact-bar__url{background:var(--blue-deep);color:var(--white);font:500 11px "Montserrat",sans-serif;padding:4px 16px;border-radius:12px}

/* ---------- FRONT ---------- */
.front__header{left:0;top:0;width:660px;height:205px;background:linear-gradient(135deg,var(--blue-deep),#00479a)}
.front__photo{left:0;top:0;width:660px;height:238px;background:linear-gradient(160deg,#c9cfd3 0%,#9db9cc 35%,#5fa6cf 60%,#b5b0a4 100%);clip-path:polygon(385px 0,660px 0,660px 238px,392px 238px,326px 108px)}
.front__photo-edge{left:0;top:0;width:660px;height:238px;background:var(--white);clip-path:polygon(380px 0,385px 0,326px 108px,392px 238px,386px 238px,320px 108px)}
.headline{left:30px;top:30px;width:290px;text-align:center}
.headline__earn,.headline__cash{display:block;font:900 60px "Montserrat",sans-serif;line-height:.95;color:var(--yellow);letter-spacing:1px}
.headline__unlimited{display:block;font:800 35px "Montserrat",sans-serif;line-height:1;color:var(--white);margin:2px 0 4px}
.flood-band{left:0;top:200px;width:392px;height:36px;background:var(--yellow);clip-path:polygon(0 0,372px 0,392px 36px,0 36px);display:flex;align-items:center;padding-left:38px;font:800 19px "Montserrat",sans-serif;color:var(--blue-deep);letter-spacing:.3px}

.cash-pill{left:30px;top:243px;width:322px;height:32px;background:var(--red);border-radius:16px;display:flex;align-items:center;padding:0 12px;color:var(--white);gap:6px;box-shadow:0 2px 0 #8f0f14}
.cash-pill__amount{font:800 25px "Montserrat",sans-serif}
.cash-pill__amount sup{font-size:13px;vertical-align:10px}
.cash-pill__small{font:700 10px "Montserrat",sans-serif;line-height:1}
.cash-pill__or{width:38px;height:38px;border-radius:50%;background:var(--white);color:var(--ink);font:900 14px "Montserrat",sans-serif;display:flex;align-items:center;justify-content:center;margin:0 2px}

.premier-tab{left:415px;top:228px;width:150px;height:17px;background:var(--gold);border-radius:8px 8px 0 0;color:#f8e7a8;font:700 10px "Montserrat",sans-serif;letter-spacing:7px;text-align:center;line-height:17px}
.partner-ribbon{left:385px;top:245px;width:262px;height:32px;display:flex;align-items:center}
.partner-ribbon__left{flex:1;height:100%;background:var(--red);border-radius:16px 0 0 16px;color:var(--white);font:700 17px "Montserrat",sans-serif;display:flex;align-items:center;padding-left:12px}
.partner-ribbon__right{flex:1.15;height:100%;background:var(--gray);border-radius:0 16px 16px 0;color:var(--white);font:700 17px "Montserrat",sans-serif;display:flex;align-items:center;justify-content:flex-end;padding-right:12px}
.partner-ribbon__badge{position:absolute;left:107px;top:-3px;width:30px;height:38px}

.wins-title{left:0;top:281px;width:660px;text-align:center;font:800 15px "Montserrat",sans-serif;color:var(--blue-deep)}
.benefits{left:72px;top:303px;width:510px;display:flex;justify-content:space-between}
.benefit{width:108px;position:relative}
.benefit__tag{height:24px;background:var(--blue-deep);border-radius:12px;display:flex;align-items:center;gap:4px;padding:0 6px;color:var(--white);font:600 7.5px "Montserrat",sans-serif;line-height:1.05;text-align:center}
.benefit__tag span{flex:1}
.benefit__tag svg{width:18px;height:18px;flex:none}
.benefit__text{margin:3px 0 0 0;height:34px;border-right:1.5px solid var(--blue-deep);border-bottom:1.5px solid var(--blue-deep);border-bottom-right-radius:8px;padding:4px 6px 0 4px;font:600 6.6px "Montserrat",sans-serif;color:var(--ink);text-align:center;line-height:1.25;position:relative}
.benefit__text::after{content:"";position:absolute;left:-2px;bottom:-3px;width:4px;height:4px;border-radius:50%;background:var(--blue-deep)}

.slogan-band{left:0;top:372px;width:660px;height:28px;background:var(--blue-mist);text-align:center;font:800 14px "Montserrat",sans-serif;color:var(--blue-deep);line-height:28px}
.slogan-band em{font-style:normal;color:var(--red)}

/* ---------- BACK ---------- */
.back__header{left:0;top:0;width:660px;height:235px;background:linear-gradient(135deg,var(--blue-deep),#0049a0)}
.back__photo{left:0;top:0;width:660px;height:235px;background:linear-gradient(150deg,#d9dcd6 0%,#b9c1b8 40%,#8fb9b0 55%,#cfcfc6 100%);clip-path:polygon(405px 0,660px 0,660px 235px,330px 235px)}
.back__headline{left:88px;top:36px;width:260px}
.back__small{display:block;font:400 22px "Archivo Black",sans-serif;line-height:1.1;color:var(--white);letter-spacing:1px}
.back__big{display:block;font:400 60px "Archivo Black",sans-serif;line-height:.95;color:var(--yellow);letter-spacing:1px}
.back__big--earn{font-size:68px}

.how-pill{left:250px;top:218px;width:300px;height:32px;background:var(--red);border-radius:16px;color:var(--white);font:400 18px "Archivo Black",sans-serif;letter-spacing:1px;display:flex;align-items:center;justify-content:center}
.steps{left:22px;top:258px;width:616px;display:flex;justify-content:space-between}
.step{width:192px;height:122px;border:2px solid var(--navy);border-radius:12px;background:var(--blue-mist);overflow:hidden;text-align:center}
.step__image{height:62px}
.step__image--floor{background:linear-gradient(150deg,#7fb3d6,#4e8fbf 50%,#cfd3d4)}
.step__image--estimate{background:linear-gradient(160deg,#9ec8ea,#5fa0d6 50%,#7a9b6e)}
.step__image--share{background:linear-gradient(170deg,#3f8ed8,#a9d0f0 60%,#e4eef6)}
.step__title{font:400 10.5px "Archivo Black",sans-serif;color:var(--blue-deep);line-height:1.05;margin-top:6px;padding:0 6px}
.step__text{font:400 8px "Roboto",sans-serif;color:var(--ink);line-height:1.2;margin-top:3px}

.refer-line{left:0;top:384px;width:660px;text-align:center;font:400 13px "Archivo Black",sans-serif;color:var(--blue-deep);letter-spacing:.3px}
.refer-line em{font-style:normal;color:var(--red)}
.flyer--back .contact-bar{height:24px}
</style>
</head>
<body>

<section class="flyer flyer--back" aria-label="Referral flyer back side">
  <div class="abs back__header"></div>
  <div class="abs back__photo" role="img" aria-label="Photo of hundred-dollar bills with letter tiles spelling cash flow"></div>
  <h2 class="abs back__headline">
    <span class="back__small">THE MORE YOU</span>
    <span class="back__big">REFER</span>
    <span class="back__small">THE MORE YOU</span>
    <span class="back__big back__big--earn">EARN</span>
  </h2>

  <div class="abs steps">
    <article class="step">
      <div class="step__image step__image--floor" role="img" aria-label="Photo of drying fans and dehumidifier on a tiled floor"></div>
      <h3 class="step__title">REFER FLOOD, MOLD &amp; CONSTRUCTION JOBS</h3>
      <p class="step__text">It's Simple to Refer 24/7:<br>Call, Text or Book Online.</p>
    </article>
    <article class="step">
      <div class="step__image step__image--estimate" role="img" aria-label="Photo of a person holding an estimate clipboard in front of a house"></div>
      <h3 class="step__title">WE TAKE CARE OF EVERYTHING</h3>
      <p class="step__text">We Schedule a Free Estimate.<br>If Approved, You Get Paid.</p>
    </article>
    <article class="step">
      <div class="step__image step__image--share" role="img" aria-label="Photo of a yellow road sign reading get paid to share against a cloudy sky"></div>
      <h3 class="step__title">EVERYBODY BENEFITS FROM REFERRALS</h3>
      <p class="step__text">We Provide Expert Quality<br>Work for Affordable Price.</p>
    </article>
  </div>
  <div class="abs how-pill">HOW IT WORKS</div>

  <p class="abs refer-line"><em>REFER:</em> FLOODS, REMODELS, RENOVATIONS &amp; REPAIRS</p>
  <footer class="contact-bar">
    <span class="contact-bar__label">CALL TEXT OR BOOK ON-LINE</span>
    <span class="contact-bar__phone">858-472-6190</span>
    <span class="contact-bar__url">BrightKeelRebuilds.com</span>
  </footer>
</section>

<section class="flyer flyer--front" aria-label="Referral flyer front side">
  <div class="abs front__header"></div>
  <div class="abs front__photo" role="img" aria-label="Photo of air movers and dehumidifiers drying a flooded room"></div>
  <div class="abs front__photo-edge"></div>

  <h1 class="abs headline">
    <span class="headline__earn">EARN</span>
    <span class="headline__unlimited">UNLIMITED</span>
    <span class="headline__cash">CASH</span>
  </h1>

  <div class="abs flood-band">GET PAID TO REFER A FLOOD</div>

  <div class="abs cash-pill">
    <span class="cash-pill__amount"><sup>$</sup>500</span>
    <span class="cash-pill__small">MINIMUM</span>
    <span class="cash-pill__or">OR</span>
    <span class="cash-pill__amount">10%</span>
    <span class="cash-pill__small">PER<br>REFERRAL!</span>
  </div>

  <div class="abs premier-tab">PREMIER</div>
  <div class="abs partner-ribbon">
    <span class="partner-ribbon__left">PARTNER</span>
    <span class="partner-ribbon__right">PROGRAM</span>
    <svg class="partner-ribbon__badge" viewBox="0 0 30 38" aria-hidden="true">
      <path d="M15 1 L28 6 V18 C28 27 22 33 15 37 C8 33 2 27 2 18 V6 Z" fill="#D4A521" stroke="#8a6a10" stroke-width="1.5"/>
      <path d="M8 18 L13 24 L23 12" fill="none" stroke="#ffffff" stroke-width="3.5" stroke-linecap="round" stroke-linejoin="round"/>
    </svg>
  </div>

  <h2 class="abs wins-title">PARTNER WITH US &amp; EVERYBODY WINS!</h2>

  <div class="abs benefits">
    <div class="benefit">
      <div class="benefit__tag">
        <svg viewBox="0 0 20 20" aria-hidden="true"><circle cx="10" cy="10" r="8" fill="#F6C407"/><circle cx="10" cy="10" r="5" fill="none" stroke="#0054AA" stroke-width="1.3"/><path d="M7.5 10 L9.3 11.8 L12.6 8.2" fill="none" stroke="#0054AA" stroke-width="1.5" stroke-linecap="round"/></svg>
        <span>GUARANTEED<br>PAYOUT</span>
      </div>
      <p class="benefit__text">Minimum $500 or 10% of Total Invoice Paid Fast</p>
    </div>
    <div class="benefit">
      <div class="benefit__tag">
        <svg viewBox="0 0 20 20" aria-hidden="true"><rect x="3" y="2" width="11" height="15" rx="1.5" fill="#F6C407"/><path d="M5.5 6h6M5.5 9h4" stroke="#0054AA" stroke-width="1.3"/><circle cx="12" cy="12" r="3" fill="#0054AA" stroke="#F6C407" stroke-width="1.3"/><path d="M14 14l3 3" stroke="#F6C407" stroke-width="1.6" stroke-linecap="round"/></svg>
        <span>FREE<br>ESTIMATES</span>
      </div>
      <p class="benefit__text">Fast &amp; Free Inspections &amp; Written Estimates</p>
    </div>
    <div class="benefit">
      <div class="benefit__tag">
        <svg viewBox="0 0 20 20" aria-hidden="true"><circle cx="11" cy="6" r="4" fill="#F6C407"/><rect x="9.5" y="10" width="3" height="2" fill="#F6C407"/><path d="M2 15 h5 l4 1.5 h5 v2 H2 Z" fill="#F6C407"/></svg>
        <span>AFFORDABLE<br>SOLUTIONS</span>
      </div>
      <p class="benefit__text">Lowest Out of Pocket Costs for Your Customers</p>
    </div>
    <div class="benefit">
      <div class="benefit__tag">
        <svg viewBox="0 0 20 20" aria-hidden="true"><circle cx="10" cy="6" r="3.2" fill="#F6C407"/><path d="M4 17 C4 12 7 10.5 10 10.5 C13 10.5 16 12 16 17 Z" fill="#F6C407"/><path d="M3 3l1 2M17 3l-1 2M10 0.8v1.6" stroke="#F6C407" stroke-width="1.2"/></svg>
        <span>INDUSTRY<br>LEADERS</span>
      </div>
      <p class="benefit__text">Licensed &amp; Certified Experts Provide 100% Guarantee</p>
    </div>
  </div>

  <p class="abs slogan-band">SEND <em>REFERRAL</em>. GET <em>PAID</em>. GROW <em>YOUR BUSINESS</em>.</p>

  <footer class="contact-bar">
    <span class="contact-bar__label">CALL TEXT OR BOOK ON-LINE</span>
    <span class="contact-bar__phone">858-472-6190</span>
    <span class="contact-bar__url">BrightKeelRebuilds.com</span>
  </footer>
</section>

</body>
</html>
```